DL Flyer announcing opening of Willow Fern Cottage Homewares & Gift Store

To create 2 sided full colour DL Flyer which will be distributed by a letterbox drop to announce the opening of a delightful new homewares and gift store called "Willow Fern Cottage Homewares" at 174 Garnet Hill Street, Ashwood.

Willow Fern Cottage Homewares offers a range of exclusive, bespoke, well-crafted decorative homewares and gifts. Our target market is well to do and aspirational, so we want the design of the flyer to match.

The owners, Maureen (a long-time resident of Northbridge) and Lorna have combined their love of homewares and years of retail experience to create this fresh and exciting new store.

Willow Fern Cottage will cater for all those special occasions throughout the year but right now as we move into Christmas we have some beautiful Christmas decorations. Why not come in and visit Lorna who has 18 years experience in the Christmas industry and find out about our Christmas Tree decorating service.

Also we want a call to action so want to offer a 10% discount for people who bring the flyer in during the month of November

The store is open Tuesday to Friday 9.30am to 5.00pm and Saturday 10.00am to 4.00pm

Please find attached duck design we are using the coloured version (excluding the word 'duck' of course). The colour we have chosen for Willow Fern Cottage is "Duck Egg Blue" and the font is Lucida Calligraphy.

Thank you

Target Market(s)

is well to do and aspirational

• Lucida Calligraphy

Colors
cfeae6

Requirements
Must have
• the Duck. Discount voucher, address, look forward to being of service for many years to come. "Duck Egg Blue" colour tones

```html
<!DOCTYPE html>
<html lang="en">
<head>
<meta charset="utf-8">
<title>Willow Fern Cottage Homewares – DL Flyer</title>
<link rel="stylesheet" href="https://fonts.googleapis.com/css2?family=Cormorant+Garamond:ital,wght@1,500;1,600&family=Open+Sans:wght@600&display=swap">
<style>
  :root {
    --backdrop: #0c0a0c;
    --duck-egg-deep: #9dc5cd;
    --duck-egg-light: #cbe7e3;
    --teal-ink: #1e6a8a;
    --diamond: #0f5f82;
    --body-ink: #4a4a4a;
    --white: #ffffff;
    --cream: #ede3da;
  }
  * { margin: 0; padding: 0; box-sizing: border-box; }
  html, body { width: 1200px; height: 1200px; overflow: hidden; background: var(--backdrop); }
  .canvas { position: relative; width: 1200px; height: 1200px; }
  .flyer { position: absolute; top: 82px; width: 492px; height: 1034px; }
  .flyer--front { left: 94px; background: var(--duck-egg-deep); }
  .flyer--back { left: 614px; background: var(--duck-egg-light); }
  .card { position: absolute; left: 50px; top: 182px; width: 392px; height: 800px; border-radius: 56px; }
  .flyer--front .card { background: var(--duck-egg-light); }
  .flyer--back .card { background: var(--duck-egg-deep); }
  .illustration { position: absolute; left: 92px; top: 128px; width: 310px; height: 188px; border-radius: 40px; }
  .flyer--front .illustration { background: radial-gradient(ellipse at 40% 55%, var(--cream) 0%, #d9ddd6 55%, var(--duck-egg-light) 100%); }
  .flyer--back .illustration { background: radial-gradient(ellipse at 40% 55%, #7fb3c2 0%, #8fbdc8 55%, var(--duck-egg-deep) 100%); }
  .text { position: absolute; left: 0; width: 100%; text-align: center; font-family: "Open Sans", sans-serif; font-weight: 600; color: var(--body-ink); }
  .intro { top: 375px; font-size: 16px; line-height: 30px; }
  .store-name { top: 487px; font-family: "Cormorant Garamond", serif; font-style: italic; font-weight: 600; color: var(--teal-ink); font-size: 50px; line-height: 46px; }
  .address { top: 630px; font-size: 16.5px; line-height: 25px; }
  .body-copy { top: 755px; left: 58px; width: 376px; font-size: 15.5px; line-height: 24px; }
  .offer { top: 390px; font-family: "Cormorant Garamond", serif; font-style: italic; font-weight: 500; color: var(--white); }
  .offer .pct { display: block; font-size: 60px; line-height: 50px; }
  .offer .word { display: block; font-size: 70px; line-height: 62px; }
  .offer-terms { top: 568px; font-size: 16.5px; line-height: 32px; }
  .hours { top: 761px; font-size: 15.5px; line-height: 30.6px; }
  .divider { position: absolute; left: 85px; top: 706px; width: 322px; height: 20px; }
</style>
</head>
<body>
<div class="canvas">
  <section class="flyer flyer--front">
    <div class="card"></div>
    <div class="illustration" role="img" aria-label="Illustration of a white duck with the brand lettering beside it"></div>
    <p class="text intro">The opening of a<br>delightful new homewares<br>and gift store</p>
    <h1 class="text store-name">Willow Fern<br>Cottage<br>Homewares</h1>
    <p class="text address">at 174 Garnet Hill Street,<br>Ashwood.</p>
    <svg class="divider" viewBox="0 0 322 20" aria-hidden="true">
      <line x1="0" y1="10" x2="121" y2="10" stroke="#0f5f82" stroke-width="1.5"/>
      <line x1="201" y1="10" x2="322" y2="10" stroke="#0f5f82" stroke-width="1.5"/>
      <polygon points="137,1 146,10 137,19 128,10" fill="#0f5f82"/>
      <polygon points="161,1 170,10 161,19 152,10" fill="#0f5f82"/>
      <polygon points="185,1 194,10 185,19 176,10" fill="#0f5f82"/>
    </svg>
    <p class="text body-copy">Willow Fern Cottage will cater for all those special occasions throughout the year but right now as we move into Christmas we have some beautiful Christmas decorations. Why not come in and visit Lorna who has 18 years experience in the Christmas industry and find out about our Christmas Tree decorating service.</p>
  </section>

  <section class="flyer flyer--back">
    <div class="card"></div>
    <div class="illustration" role="img" aria-label="Blue line illustration of a duck with the brand lettering beside it"></div>
    <h2 class="text offer"><span class="pct">10%</span><span class="word">Discount</span></h2>
    <p class="text offer-terms">for people who bring<br>the flyer in during<br>the month of November</p>
    <svg class="divider" viewBox="0 0 322 20" aria-hidden="true">
      <line x1="0" y1="10" x2="121" y2="10" stroke="#0f5f82" stroke-width="1.5"/>
      <line x1="201" y1="10" x2="322" y2="10" stroke="#0f5f82" stroke-width="1.5"/>
      <polygon points="137,1 146,10 137,19 128,10" fill="#0f5f82"/>
      <polygon points="161,1 170,10 161,19 152,10" fill="#0f5f82"/>
      <polygon points="185,1 194,10 185,19 176,10" fill="#0f5f82"/>
    </svg>
    <p class="text hours">The store is open<br>Tuesday to Friday<br>9.30am to 5.00pm<br>and<br>Saturday<br>10.00am to 4.00pm</p>
  </section>
</div>
</body>
</html>
```